Glamour By Tavi

I am a makeup artist looking for professional looking double sided business card. I would like to create a logo and incorporate a set of eyes as the periods above the name "Tavi" on the card.

front of card: Logo "Glamour by Tavi" written across diagonal (bottom left to top right)

Back of card:
1) Professional makeup artist serving New York & New Jersey (or similar to this text)
2) 917-555-0148
3) glamourbytavi@mailcove.com

Industry/Entity Type

Business

```html
<!DOCTYPE html>
<html lang="en">
<head>
<meta charset="utf-8">
<title>Glamour by Tavi – Business Card</title>
<link rel="stylesheet" href="https://fonts.googleapis.com/css2?family=Quicksand:wght@300;400;500&display=swap">
<style>
  :root {
    --page-bg: #2a2a2a;
    --card-black: #0c0d0e;
    --card-glow: #2b2e31;
    --text-light: #d6d6d6;
    --text-soft: #b9b9b9;
    --icon-grey: #bdbdbd;
    --photo-dark: #140d09;
    --photo-hair: #6b3f24;
    --photo-skin: #e8b79a;
    --photo-skin-light: #f2cdb5;
  }
  * { margin: 0; padding: 0; box-sizing: border-box; }
  html, body {
    width: 1200px;
    height: 1000px;
    overflow: hidden;
    background: var(--page-bg);
  }
  .card {
    position: absolute;
    left: 172px;
    top: 258px;
    width: 866px;
    height: 475px;
    overflow: hidden;
    background: radial-gradient(ellipse 60% 70% at 50% 55%, var(--card-glow) 0%, var(--card-black) 75%);
    box-shadow: 0 6px 18px rgba(0,0,0,0.55);
    font-family: "Quicksand", sans-serif;
  }
  .portrait {
    position: absolute;
    right: 0;
    top: 0;
    width: 310px;
    height: 100%;
    background:
      radial-gradient(ellipse 70% 55% at 60% 55%, var(--photo-skin-light) 0%, var(--photo-skin) 45%, transparent 75%),
      linear-gradient(160deg, var(--photo-dark) 0%, var(--photo-hair) 30%, var(--photo-skin) 60%, var(--photo-dark) 100%);
    -webkit-mask-image: linear-gradient(90deg, transparent 0%, #000 22%);
            mask-image: linear-gradient(90deg, transparent 0%, #000 22%);
  }
  .brand {
    position: absolute;
    left: 45px;
    top: 238px;
    width: 388px;
    text-align: right;
  }
  .brand-name {
    display: block;
    font-size: 38px;
    font-weight: 400;
    color: var(--text-light);
    letter-spacing: 0.5px;
    line-height: 1;
  }
  .brand-title {
    display: block;
    margin-top: 6px;
    font-size: 13px;
    font-weight: 400;
    letter-spacing: 3px;
    color: var(--text-soft);
  }
  .contact {
    position: absolute;
    left: 133px;
    top: 341px;
    list-style: none;
  }
  .contact-item {
    display: flex;
    align-items: center;
    height: 22px;
    margin-bottom: 13px;
    font-size: 14.5px;
    font-weight: 500;
    letter-spacing: 0.6px;
    color: var(--text-light);
  }
  .contact-icon {
    width: 26px;
    height: 18px;
    margin-right: 23px;
    fill: var(--icon-grey);
  }
</style>
</head>
<body>
  <main class="card">
    <div class="portrait" role="img" aria-label="Photo of a woman having eyeshadow applied with a makeup brush"></div>

    <div class="brand">
      <span class="brand-name">Glamour by Tavi</span>
      <span class="brand-title">MAKEUP ARTIST</span>
    </div>

    <ul class="contact">
      <li class="contact-item">
        <svg class="contact-icon" viewBox="0 0 26 18" aria-hidden="true">
          <path d="M2 6 C2 2 24 2 24 6 L24 8 L18 8 L18 5.5 L8 5.5 L8 8 L2 8 Z"/>
          <path d="M6 9 L20 9 L22 17 L4 17 Z"/>
          <circle cx="13" cy="12.5" r="2.3" fill="#0c0d0e"/>
        </svg>
        917-555-0148
      </li>
      <li class="contact-item">
        <svg class="contact-icon" viewBox="0 0 26 18" aria-hidden="true">
          <rect x="1" y="2" width="24" height="14" />
          <path d="M1 2 L13 11 L25 2" fill="none" stroke="#0c0d0e" stroke-width="1.5"/>
        </svg>
        glamourbytavi@mailcove.com
      </li>
    </ul>
  </main>
</body>
</html>
```